B2B Website for manufacturer of aerospace coatings

B2B Website for manufacturer of aerospace optical coatings and screens used in flight simulators and air-traffic controller centers. We sell to both the military as well as commercial airlines.

Colors: primary colors should be white and blue (same blue as in the logo), but you can accent with red, orange, or any other colors.

Main menu: Products, Services, About Us, Contact Us

Logo = See "Hollin SkyPrism" JPEG attached.

We'd like a professional website that appeals to engineers at companies like Varnell, OKTU, the military, etc.

We intend to build this website on WordPress.

Websites we like in our industry:
https://www.plaxomodel.example/
https://www.dorvik.example/civil-aviation/aviation-simulation-equipment/training-equipment/full-flight-simulators/
https://z7works.example/
https://www.lumbrent.example/
https://quellorn.example/
https://hangarpathworks.example/

3 Pages: Homepage, Product page, Contact Us page

Target Market(s)

Varnell, Pembry Falcrest, Zelvane

Industry/Entity Type

Aerospace

Number of Pages Required

3 page

Colors
0054AA
0677BA
7BADD7
CADEEF
E8F1F8
F0912C
F2A743
F7CA91
FBE8D2
FDF5EE
EB3D1F
EC4F4E
F09395
F8D3D4
FCEDEE

Requirements
Should not have
• Black background

```html
<!DOCTYPE html>
<html lang="en">
<head>
<meta charset="utf-8">
<title>Hollin SkyPrism — Seamless Projection Screens</title>
<link rel="stylesheet" href="https://fonts.googleapis.com/css2?family=Inter:wght@300;400;500;600;700&display=swap">
<style>
:root{
  --blue:#0054AA;
  --blue-mid:#0677BA;
  --blue-light:#7BADD7;
  --blue-pale:#CADEEF;
  --ink:#141414;
  --muted:#6b6b6b;
  --grey-bg:#efefef;
  --line:#d4d4d4;
  --white:#ffffff;
  --hero-deep:#140a2a;
  --hero-violet:#5a1d8a;
  --hero-magenta:#b02e9e;
}
*{box-sizing:border-box;margin:0;padding:0}
html,body{width:1200px;height:4720px;overflow:hidden}
body{font-family:"Inter",Helvetica,Arial,sans-serif;color:var(--ink);background:var(--white);position:relative}
section,header,footer{position:absolute;left:0;width:1200px}

/* hero */
.hero{top:0;height:1088px;overflow:hidden;color:var(--white);
  background:radial-gradient(ellipse 620px 520px at 820px 420px,rgba(176,46,158,.55),transparent 70%),
  radial-gradient(ellipse 700px 600px at 1000px 700px,rgba(90,29,138,.8),transparent 70%),
  linear-gradient(135deg,#241047 0%,var(--hero-deep) 55%,#1d0d3a 100%);}
.hero-art{position:absolute;inset:0}
.nav{position:absolute;top:20px;left:28px;right:28px;display:flex;align-items:center;justify-content:space-between}
.brand{display:flex;flex-direction:column;line-height:1}
.brand-name{font-weight:700;font-size:20px;letter-spacing:1px}
.brand-sub{font-size:9px;opacity:.7;margin-top:3px;letter-spacing:.5px}
.menu{display:flex;gap:44px;align-items:center;font-size:14px}
.menu .contact{border:1px solid var(--white);border-radius:22px;padding:8px 20px}
.hero-eyebrow{position:absolute;left:176px;top:124px;font-size:14px;font-weight:600}
.hero-eyebrow::before{content:"";position:absolute;left:0;top:-28px;width:10px;height:10px;border-left:2px solid #fff;border-bottom:2px solid #fff;transform:rotate(-45deg)}
.hero-title{position:absolute;left:176px;top:190px;width:600px;font-size:52px;font-weight:600;line-height:1.12}
.scroll-hint{position:absolute;left:876px;top:490px;font-size:13px;display:flex;align-items:center;gap:12px}
.scroll-hint span{width:18px;height:18px;border:1.5px solid #fff;border-radius:50%}
.hero-copy{position:absolute;left:468px;top:628px;width:600px;font-size:22px;line-height:1.4;font-weight:300}
.hero-copy p+p{margin-top:26px}
.read-more{position:absolute;left:470px;top:888px;width:100px;height:100px;border-radius:50%;background:var(--hero-deep);border:1px solid rgba(255,255,255,.3);display:flex;align-items:center;justify-content:center;font-size:12px;font-weight:600}

/* products */
.products{top:1088px;height:900px}
.section-title{position:absolute;left:176px;top:80px;font-size:22px;font-weight:600}
.section-sub{position:absolute;left:176px;top:126px;width:420px;font-size:12px;line-height:1.45;color:var(--muted)}
.ticker{position:absolute;white-space:nowrap;font-size:84px;font-weight:300;color:var(--blue);letter-spacing:-1px}
.products .ticker{top:190px;left:-40px}
.card{position:absolute;top:360px;width:384px;height:480px;overflow:hidden;color:var(--white)}
.card-1{left:176px}
.card-2{left:640px}
.card-media{position:absolute;inset:0}
.card-1 .card-media{background:linear-gradient(180deg,#6f86a1 0%,#a9b7c4 30%,#5b5a55 48%,#2e2b27 100%)}
.card-2 .card-media{background:linear-gradient(180deg,#1c3a63 0%,#3f5f86 35%,#6c7d8f 55%,#1e2731 100%)}
.card-text{position:absolute;left:32px;bottom:34px;width:320px}
.card-text h3{font-size:24px;font-weight:600;line-height:1.15;text-decoration:underline;text-underline-offset:4px}
.card-text p{font-size:12px;line-height:1.4;margin-top:14px;opacity:.9}
.card-2 .card-text{bottom:40px}
.view-btn{position:absolute;left:240px;top:120px;width:112px;height:112px;border-radius:50%;background:var(--blue);display:flex;align-items:center;justify-content:center;text-align:center;font-size:13px;font-weight:600;line-height:1.3}

/* projects */
.projects{top:2020px;height:800px;background:var(--blue);color:var(--white);overflow:hidden}
.photo{position:absolute}
.photo-a{left:0;top:0;width:440px;height:180px;background:linear-gradient(120deg,#39342f,#8b857c 60%,#5c5650)}
.photo-b{left:820px;top:120px;width:380px;height:420px;background:linear-gradient(160deg,#4a4a4c,#9a9894 50%,#35383c)}
.photo-c{left:0;top:600px;width:440px;height:200px;background:linear-gradient(180deg,#2b2d2f,#6c716f 60%,#232527)}
.photo-d{left:980px;top:560px;width:220px;height:180px;background:linear-gradient(180deg,#7b7d80,#b3b3b0)}
.projects-label{position:absolute;left:440px;top:90px;font-size:12px;font-weight:600}
.projects-title{position:absolute;left:200px;top:120px;width:800px;text-align:center;font-size:74px;font-weight:600;line-height:1.2}
.projects-note{position:absolute;left:0;width:1200px;top:640px;text-align:center;font-size:14px;font-weight:500}
.projects-cta{position:absolute;left:0;width:1200px;top:690px;display:flex;justify-content:center;align-items:center;gap:18px;font-size:22px}
.projects-cta a{color:var(--white);text-decoration:none;border:1px solid #fff;border-radius:22px;font-size:14px;padding:8px 20px}

/* clients */
.clients{top:2820px;height:680px}
.clients-intro{position:absolute;left:176px;top:180px;width:560px;font-size:22px;line-height:1.4}
.client{position:absolute;top:300px;width:360px;height:360px;border:1px solid var(--line);border-radius:50%;display:flex;align-items:center;justify-content:center;font-size:26px;font-weight:600;letter-spacing:.5px}

/* support */
.support{top:3500px;height:820px;background:var(--grey-bg)}
.support-label{position:absolute;left:176px;top:140px;font-size:12px;font-weight:600}
.support-row{position:absolute;left:176px;width:840px;height:160px;border-bottom:1px solid var(--line);display:flex;align-items:center}
.support-row:nth-of-type(2){top:180px}
.support-row:nth-of-type(3){top:340px}
.support-row:nth-of-type(4){top:500px}
.support-row:nth-of-type(5){top:660px}
.support-thumb{width:200px;height:112px;margin-right:24px;background:radial-gradient(circle at 50% 55%,#2d7fc0 0,#174a86 40%,#0a1526 75%)}
.support-text{flex:1;font-size:22px;line-height:1.35;max-width:460px}
.more-btn{position:absolute;right:0;top:50%;margin-top:-52px;width:104px;height:104px;border-radius:50%;border:1px solid var(--line);background:var(--white);display:flex;align-items:center;justify-content:center;font-size:12px;font-weight:600}
.more-btn.is-active{background:var(--blue);color:var(--white);border-color:var(--blue)}

/* footer */
.footer{top:4320px;height:400px}
.footer .ticker{top:40px;left:-20px}
.footer-invite{position:absolute;left:176px;top:190px;font-size:20px;line-height:1.4}
.footer-bar{position:absolute;left:176px;right:176px;top:320px;display:flex;justify-content:space-between;align-items:center;font-size:12px}
.follow{display:flex;flex-direction:column;align-items:center;gap:6px}
</style>
</head>
<body>

<header class="hero">
  <div class="hero-art" role="img" aria-label="Abstract swirl of glowing violet and magenta light trails"></div>
  <nav class="nav">
    <div class="brand"><span class="brand-name">HOLLIN</span><span class="brand-sub">SkyPrism</span></div>
    <div class="menu"><span>Home</span><span>About</span><span>Products</span><span>Services</span><span class="contact">Contact Us</span></div>
  </nav>
  <div class="hero-eyebrow">Hollin SkyPrism's</div>
  <h1 class="hero-title">The World's largest manufacture of “Seamless” front and back projection screens.</h1>
  <div class="scroll-hint">Scroll to Navigate <span></span></div>
  <div class="hero-copy">
    <p>Our mission has always been to provide the highest image fidelity to every project we undertake.</p>
    <p>In fact, the Guild of Projection Arts and Sciences was so impressed, Hollin Filmscreen has been the recipient of two Guild Awards for Science and Technical achievements.</p>
  </div>
  <div class="read-more">Read More</div>
</header>

<section class="products">
  <h2 class="section-title">Our Products</h2>
  <p class="section-sub">Defense and aviation companies operate in a fast-paced field. We have deep roots in research and meet the challenge.</p>
  <div class="ticker">Small Volume &nbsp;·&nbsp; High-Quality &nbsp;·&nbsp; Quick Delivery &nbsp;·&nbsp; Small Volume</div>

  <article class="card card-1">
    <div class="card-media" role="img" aria-label="Air traffic control tower overlooking an airfield"></div>
    <div class="view-btn">View<br>Products</div>
    <div class="card-text">
      <h3>Commercial Aviation Simulation</h3>
      <p>Hollin SkyPrism produces a full range of innovative positioning devices to suit all fixed wing general aviation aircraft training needs.</p>
    </div>
  </article>
  <article class="card card-2">
    <div class="card-media" role="img" aria-label="Military vehicle simulator in front of a projected landscape"></div>
    <div class="card-text"><h3>Defense Industry Simulation</h3></div>
  </article>
</section>

<section class="projects">
  <div class="photo photo-a" role="img" aria-label="Simulator cockpit interior"></div>
  <div class="photo photo-b" role="img" aria-label="Curved projection screen installation"></div>
  <div class="photo photo-c" role="img" aria-label="Control center with operator consoles"></div>
  <div class="photo photo-d" role="img" aria-label="Screen frame under construction"></div>
  <div class="projects-label">Recent Projects</div>
  <h2 class="projects-title">We've Delivered hundreds of successful Projects for our clients.</h2>
  <p class="projects-note">Manufacturing all our screen materials in house, we have on site at our factory in Redwell, CA</p>
  <div class="projects-cta">Still Not Convinced? <a href="#">Contact Us</a></div>
</section>

<section class="clients">
  <p class="clients-intro">Some of our customer that we provide OEM and end user simulation products</p>
  <div class="client" style="left:-110px">Arkeo</div>
  <div class="client" style="left:120px">Norvane Gridwell</div>
  <div class="client" style="left:412px">OKTU</div>
  <div class="client" style="left:708px">Skyvale Training</div>
  <div class="client" style="left:1004px">Varnell</div>
</section>

<section class="support">
  <div class="support-label">Global support services: On time, every time</div>
  <div class="support-row">
    <div class="support-thumb" role="img" aria-label="Globe projected on a curved simulation screen"></div>
    <p class="support-text">Simulation laminates in any shape</p>
    <div class="more-btn is-active">More Info</div>
  </div>
  <div class="support-row">
    <p class="support-text">We are committed to servicing our installed base</p>
    <div class="more-btn">More Info</div>
  </div>
  <div class="support-row">
    <p class="support-text">Immersion spoken here</p>
    <div class="more-btn">More Info</div>
  </div>
  <div class="support-row">
    <p class="support-text">Many leading aerospace companies rely on Hollin SkyPrism</p>
    <div class="more-btn">More Info</div>
  </div>
</section>

<footer class="footer">
  <div class="ticker">SkyPrism &nbsp;·&nbsp; Hollin SkyPrism &nbsp;·&nbsp; Hollin SkyPrism</div>
  <p class="footer-invite">We would love to hear from you.<br>Let's work together</p>
  <div class="footer-bar">
    <span>Back to Top</span>
    <span>© 2022 Hollin SkyPrism. All rights reserved</span>
    <span class="follow">
      <svg width="16" height="16" viewBox="0 0 16 16" aria-hidden="true"><path d="M8 2v10M3 7l5-5 5 5" fill="none" stroke="#141414" stroke-width="1.4"/></svg>
      Follow Us
    </span>
  </div>
</footer>

</body>
</html>
```